Website Design for a "Talent Recruitment Agency"

We are looking for a website design for the website of our "Talent Recruitment Agency"; which is called "Crestline Circle".
Our recruitment website "Crestline Circle" will be focusing on: "Crestline Circle: Bridging People & Employers in Switzerland"; which means our target audience is two-folded:
(i) TALENT - that is currently residing in- or outside of Switzerland, and is open for and interested in the "Swiss Job Market".
(ii) COMPANIES - that are looking for talent for specific job vacancies in Switzerland.
With our "Crestline Circle" approach we inted to focus on Membership & Partnership:
(a)"Membership"(TALENT)
and
(b)"Partnership"(COMPANIES)
Some of the competitor sites we like are:
• www.brimlo42.dk
• www.qazet.ch
• www.plovik.ch/en
A sitemap example of our website is attached.
Also attached is a "Crestline Circle" logo in .eps format and one in .jpeg format.
We very much look forward to receive your creative ideas.
Best regards,
Crestline Circle
Crestline Circle: Bridging People & Employers in Switzerland.
Website: crestlinecircle.ch - Twitter: CrestlineCircleCH
Target Market(s)
(i) TALENT (with around 0-10 years of working experience), currently residing in- or outside of Switzerland, but eligible to work in Switzerland.
(ii) COMPANIES (national or international) that are based in Switzerland.
Industry/Entity Type
Recruitment

```html
<!DOCTYPE html>
<html lang="en">
<head>
<meta charset="utf-8">
<title>Crestline Circle – Home</title>
<link href="https://fonts.googleapis.com/css2?family=Open+Sans:wght@400;600&family=Ubuntu:wght@400;500;700&display=swap" rel="stylesheet">
<style>
:root{
  --blue:#0a7fcf;
  --blue-deep:#0673bd;
  --blue-band:#2f8cca;
  --blue-dark:#05609f;
  --orange:#f0602a;
  --text:#555;
  --muted:#8a8a8a;
  --page:#f6f6f6;
  --hero:#e9e9e9;
  --line:#e2e2e2;
  --white:#fff;
}
*{box-sizing:border-box;margin:0;padding:0}
html,body{width:698px;height:1200px;overflow:hidden}
body{position:relative;background:var(--page);font-family:"Open Sans",sans-serif;color:var(--text)}
.abs{position:absolute}
.top-strip{left:0;top:0;width:698px;height:6px;background:#e4e4e4}
.brand{left:38px;top:31px;display:flex;align-items:center;gap:8px}
.brand-dot{width:26px;height:26px;border-radius:50%;background:var(--orange)}
.brand-name{font-family:"Ubuntu",sans-serif;font-weight:500;font-size:20px;color:var(--blue)}
.lang{right:40px;top:26px;display:flex;align-items:center;gap:3px;font-size:6.5px;color:var(--muted)}
.lang-label{margin-right:4px}
.lang-chip{width:8px;height:7px}
.social-top{right:40px;top:47px;display:flex;gap:5px}
.circle-icon{width:16px;height:16px;border-radius:50%;background:#2a7fc0}
.nav{left:0;top:78px;width:698px;height:25px;background:var(--blue)}
.nav a{position:absolute;top:0;height:25px;line-height:25px;font-size:9px;letter-spacing:.8px;color:var(--white);text-decoration:none;text-transform:uppercase}
.nav .active{background:#2b93dc;padding:0 7px}
.search{left:540px;top:3px;width:122px;height:19px;background:var(--white);border:1px solid #cfcfcf;font-size:7.5px;line-height:17px;padding-left:5px;color:#777}
.search svg{position:absolute;right:4px;top:3px}
.hero{left:0;top:103px;width:698px;height:246px;background:var(--hero)}
.hero-art{left:76px;top:128px;width:176px;height:221px;border-radius:90px 90px 0 0;background:radial-gradient(circle at 50% 35%,#f3a45a 0%,#c66aa8 35%,#5aa6d8 65%,#e9e9e9 100%);opacity:.75}
.hero-title{left:328px;top:146px;width:340px;font-family:"Ubuntu",sans-serif;font-weight:700;font-size:17px;line-height:20px;letter-spacing:1.4px;text-transform:uppercase}
.hero-title .o{color:var(--orange)}
.hero-title .b{color:var(--blue)}
.hero-copy{left:328px;top:212px;width:300px;font-size:9.6px;line-height:12.8px;color:#666}
.hero-copy p+p{margin-top:6px}
.btn{display:block;background:var(--blue);color:var(--white);text-align:center;text-transform:uppercase;font-size:8.5px;letter-spacing:.8px}
.hero-btn{left:329px;top:300px;width:93px;height:22px;line-height:22px}
.section-title{font-family:"Ubuntu",sans-serif;font-size:12px;letter-spacing:.6px;text-transform:uppercase;color:var(--blue)}
.section-title span{color:var(--orange)}
.about-title{left:64px;top:385px;width:374px;padding-bottom:7px;border-bottom:1px solid var(--line)}
.about-copy{left:65px;top:421px;width:378px;font-size:9.4px;line-height:12.4px}
.about-copy p+p{margin-top:12px}
.testimonials{left:470px;top:386px;width:171px;height:184px;background:var(--white);border:1px solid #e0e0e0;border-bottom:3px solid #ddd}
.t-head{height:22px;background:var(--blue);color:var(--white);font-size:8px;line-height:22px;padding-left:10px;position:relative}
.t-dots{position:absolute;right:10px;top:8px;display:flex;gap:3px}
.t-dots i{width:5px;height:5px;border-radius:50%;background:var(--white)}
.t-dots i:first-child{background:var(--orange)}
.t-item{position:relative;height:70px;margin:0 8px;border-bottom:1px solid #e6e6e6}
.t-item:last-child{border-bottom:none}
.t-photo{position:absolute;left:2px;top:12px;width:32px;height:40px;background:linear-gradient(#c9b7a6,#6b6058);border:1px solid #bbb}
.t-text{position:absolute;left:41px;top:12px;width:112px;font-size:7.3px;line-height:9.5px;color:#666}
.t-name{color:var(--orange);margin-top:4px;display:block}
.more-title{left:72px;top:586px}
.rule{height:1px;background:var(--line)}
.rule-more{left:62px;top:612px;width:560px}
.feature{width:170px;text-align:center}
.feature svg{display:block;margin:0 auto}
.feature h3{font-family:"Ubuntu",sans-serif;font-weight:400;font-size:10px;letter-spacing:.8px;color:var(--blue);margin-top:14px}
.feature p{font-size:8.5px;line-height:12.2px;margin-top:5px}
.feature .btn{width:66px;height:15px;line-height:15px;font-size:7px;letter-spacing:.3px;text-transform:none;margin:13px auto 0}
.rule-partners{left:62px;top:848px;width:560px}
.partners{left:70px;top:892px;width:556px;display:flex;justify-content:space-between;align-items:center}
.partner{height:20px;border-radius:3px;background:#c9c9c9}
.newsletter{left:0;top:954px;width:698px;height:56px;background:var(--blue-band)}
.news-brand{left:48px;top:976px;display:flex;align-items:center;gap:6px}
.news-brand .brand-dot{width:18px;height:18px;background:#7cc8f2}
.news-brand .brand-name{font-size:13px;color:#9fdcff}
.news-input{left:176px;top:972px;width:377px;height:26px;background:var(--white);border-radius:2px;font-size:10px;line-height:26px;padding-left:10px;color:#999;letter-spacing:.3px}
.subscribe{left:558px;top:972px;width:72px;height:26px;line-height:26px;background:var(--orange);color:var(--white);text-align:center;font-size:10px;letter-spacing:.4px}
.footer{left:0;top:1010px;width:698px;height:166px;background:var(--blue-deep)}
.f-head{font-size:9px;letter-spacing:.8px;text-transform:uppercase;color:var(--white);padding-bottom:7px;border-bottom:1px solid rgba(255,255,255,.2)}
.f-links{list-style:none;font-size:7.6px;line-height:13.6px;color:var(--white);letter-spacing:.3px}
.f-social{left:62px;top:1120px;display:flex;gap:4px}
.f-social i{width:14px;height:14px;border-radius:50%;background:var(--white)}
.field{background:var(--white);font-size:7.5px;color:#888;padding-left:5px;border-radius:1px}
.send{left:464px;top:1136px;width:93px;height:21px;line-height:21px;background:var(--orange);color:var(--white);text-align:center;font-size:7.5px;letter-spacing:.6px;border-radius:2px}
.bottom{left:0;top:1176px;width:698px;height:24px;background:var(--blue-dark);color:var(--white);font-size:7.5px;line-height:24px;padding-left:63px;letter-spacing:.3px}
</style>
</head>
<body>
<div class="abs top-strip"></div>

<header>
  <div class="abs brand"><span class="brand-dot"></span><span class="brand-name">Crestline Circle</span></div>
  <div class="abs lang"><span class="lang-label">Select Language:</span>
    <span class="lang-chip" style="background:#e0262a"></span>
    <span class="lang-chip" style="background:#cf3a3a"></span>
    <span class="lang-chip" style="background:#2d3f86"></span>
    <span class="lang-chip" style="background:#2a4aa0"></span>
  </div>
  <div class="abs social-top"><span class="circle-icon" style="background:#5b9fd4"></span><span class="circle-icon" style="background:#3b5a96"></span><span class="circle-icon" style="background:#1d7ab8"></span></div>
  <nav class="abs nav">
    <a class="active" style="left:42px">Home</a>
    <a style="left:114px">About</a>
    <a style="left:186px">Talents</a>
    <a style="left:266px">Companies</a>
    <a style="left:362px">Events</a>
    <a style="left:438px">Contact</a>
    <div class="abs search">Keyword Search...
      <svg width="12" height="12" viewBox="0 0 12 12"><circle cx="5" cy="5" r="3.5" fill="none" stroke="#999" stroke-width="1.3"/><line x1="7.5" y1="7.5" x2="11" y2="11" stroke="#999" stroke-width="1.6"/></svg>
    </div>
  </nav>
</header>

<section>
  <div class="abs hero"></div>
  <div class="abs hero-art" role="img" aria-label="Colourful tree illustration of branching lines ending in circles with people"></div>
  <h1 class="abs hero-title"><span class="o">Crestline Circle: Bridging</span><br><span class="o">People </span><span class="b">&amp; Employers</span><br><span class="b">in Switzerland</span></h1>
  <div class="abs hero-copy">
    <p>Lorem ipsum dolor sit amet, consectetur adipiscing elit. Phasellus tincidunt tellus leo, sodales vestibulum urna hendrerit vel. Maecenas ut pretium tortor asellus tin tellus leo.</p>
    <p>Adales vestibulum urna hendrerit vel. Maecenas ut pretium tortor asellus tin tellus leo, sodales vestibulum urna.</p>
  </div>
  <a class="abs btn hero-btn">Read more</a>
</section>

<section>
  <h2 class="abs section-title about-title">About <span>Crestline Circle</span></h2>
  <div class="abs about-copy">
    <p>Lorem ipsum dolor sit amet, consectetur adipiscing elit. Phasellus eget leo leo. Sed adipiscing mi orci, vel ultrices turpis mattis a. Quisque sed eros luctus, euismod ligula et, suscipit dolor. Sed suscipit tortor eget leo hendrerit semper. Sed et fermentum erat.</p>
    <p>Curabitur tristique vestibulum bibendum. Quisque eget varius eros. Nunc id laoreet sem. Nullam vulputate fringilla mi sit amet imperdiet. Lorem ipsum dtolor sit amet, consectetur adipiscing elit. Pellentesque habitant morbi tristique senectus et netus et malesuada fames ac turpis egestas.</p>
  </div>
  <aside class="abs testimonials">
    <div class="t-head">Testimonials<span class="t-dots"><i></i><i></i><i></i></span></div>
    <div class="t-item">
      <div class="t-photo" role="img" aria-label="Portrait photo of a smiling man"></div>
      <p class="t-text">Lorem ipsum dolor sit amet, consect adipiscing elit. Phasellus eget leo. Sed lipsum dolor mi orci<span class="t-name">- Lena Marsh, Talent</span></p>
    </div>
    <div class="t-item">
      <div class="t-photo" role="img" aria-label="Portrait photo of a man in a suit"></div>
      <p class="t-text">Lorem ipsum dolor sit amet, consect adipiscing elit. Phasellus eget leo. Sed lipsum dolor mi orci<span class="t-name">- Tobias Keller, Manager</span></p>
    </div>
  </aside>
</section>

<section>
  <h2 class="abs section-title more-title">More <span>About Us</span></h2>
  <div class="abs rule rule-more"></div>

  <div class="abs feature" style="left:64px;top:646px">
    <svg width="76" height="54" viewBox="0 0 76 54">
      <circle cx="16" cy="16" r="8" fill="var(--blue)"/><path d="M2 44 Q2 26 16 26 Q30 26 30 44Z" fill="var(--blue)"/>
      <circle cx="60" cy="16" r="8" fill="var(--blue)"/><path d="M46 44 Q46 26 60 26 Q74 26 74 44Z" fill="var(--blue)"/>
      <circle cx="38" cy="13" r="11" fill="var(--orange)"/><path d="M18 50 Q18 26 38 26 Q58 26 58 50Z" fill="var(--orange)"/>
    </svg>
    <h3>TALENTS</h3>
    <p>Lorem ipsum dolor sit amet, sectetur adipiscing elit. Ut felis ligula, dignissim sit amet Adum non, lobortis eget lacus.</p>
    <a class="btn">More details</a>
  </div>

  <div class="abs feature" style="left:263px;top:646px">
    <svg width="54" height="54" viewBox="0 0 54 54">
      <path d="M22 6 L44 2 L52 8 L52 54 L22 54Z" fill="var(--blue)"/>
      <path d="M2 14 L22 10 L22 54 L2 54Z" fill="var(--orange)"/>
      <g fill="#fff"><rect x="6" y="18" width="5" height="4"/><rect x="13" y="18" width="5" height="4"/><rect x="6" y="27" width="5" height="4"/><rect x="13" y="27" width="5" height="4"/><rect x="6" y="36" width="5" height="4"/><rect x="13" y="36" width="5" height="4"/>
      <rect x="27" y="14" width="5" height="5"/><rect x="35" y="14" width="5" height="5"/><rect x="27" y="24" width="5" height="5"/><rect x="35" y="24" width="5" height="5"/><rect x="27" y="34" width="5" height="5"/><rect x="35" y="34" width="5" height="5"/><rect x="27" y="44" width="5" height="5"/><rect x="35" y="44" width="5" height="5"/></g>
    </svg>
    <h3>COMPANIES</h3>
    <p>Lorem ipsum dolor sit amet, sectetur adipiscing elit. Ut felis ligula, dignissim sit amet Adum non, lobortis eget lacus.</p>
    <a class="btn">More details</a>
  </div>

  <div class="abs feature" style="left:461px;top:646px">
    <svg width="44" height="54" viewBox="0 0 44 54">
      <rect x="2" y="8" width="40" height="44" fill="none" stroke="var(--blue)" stroke-width="3"/>
      <rect x="2" y="8" width="40" height="9" fill="var(--orange)"/>
      <rect x="10" y="3" width="3" height="9" fill="var(--orange)"/><rect x="31" y="3" width="3" height="9" fill="var(--orange)"/>
      <g fill="var(--blue)"><rect x="7" y="21" width="7" height="6"/><rect x="16" y="21" width="7" height="6"/><rect x="25" y="21" width="7" height="6"/><rect x="34" y="21" width="5" height="6"/>
      <rect x="7" y="30" width="7" height="6"/><rect x="16" y="30" width="7" height="6"/><rect x="25" y="30" width="7" height="6"/><rect x="34" y="30" width="5" height="6"/>
      <rect x="7" y="39" width="7" height="6"/><rect x="16" y="39" width="7" height="6"/><rect x="25" y="39" width="7" height="6"/><rect x="34" y="39" width="5" height="6"/></g>
    </svg>
    <h3>EVENTS</h3>
    <p>Lorem ipsum dolor sit amet, sectetur adipiscing elit. Ut felis ligula, dignissim sit amet Adum non, lobortis eget lacus.</p>
    <a class="btn">More details</a>
  </div>

  <div class="abs rule rule-partners"></div>
  <div class="abs partners" aria-label="Partner companies">
    <span class="partner" style="width:66px"></span>
    <span class="partner" style="width:96px"></span>
    <span class="partner" style="width:62px;height:28px"></span>
    <span class="partner" style="width:98px;height:14px"></span>
    <span class="partner" style="width:88px"></span>
  </div>
</section>

<footer>
  <div class="abs newsletter"></div>
  <div class="abs news-brand"><span class="brand-dot"></span><span class="brand-name">Crestline Circle</span></div>
  <div class="abs news-input">Send us your Email to Join our monthly Newsletter</div>
  <div class="abs subscribe">Subscribe</div>

  <div class="abs footer"></div>
  <div class="abs" style="left:58px;top:1027px;width:145px">
    <h4 class="f-head">Quicklinks</h4>
    <ul class="f-links" style="display:grid;grid-template-columns:81px 60px;margin:6px 0 0 5px">
      <li>Home</li><li>Events</li><li>About</li><li>Contact</li><li>Talents</li><li></li><li>Companies</li>
    </ul>
  </div>
  <div class="abs f-social"><i></i><i></i><i></i><i></i></div>

  <div class="abs" style="left:266px;top:1027px;width:123px">
    <h4 class="f-head">Useful Information</h4>
    <ul class="f-links" style="margin:6px 0 0 4px">
      <li>Sitemap</li><li>F.A.Q</li><li>Privacy Policy</li><li>Terms &amp; Conditions</li>
    </ul>
  </div>

  <div class="abs" style="left:461px;top:1027px;width:169px">
    <h4 class="f-head">Quick Message</h4>
  </div>
  <div class="abs field" style="left:463px;top:1058px;width:80px;height:16px;line-height:16px">Firstname</div>
  <div class="abs field" style="left:548px;top:1058px;width:80px;height:16px;line-height:16px">Email Address</div>
  <div class="abs field" style="left:463px;top:1079px;width:165px;height:51px;padding-top:3px">Message</div>
  <div class="abs send">SEND MESSAGE</div>

  <div class="abs bottom">Crestline Circle Copyright 2014 &nbsp;All rights reserved</div>
</footer>
</body>
</html>
```